Coldbrook IT
Business Cards & Stationary
Hi everyone,
Thanks a lot for your efforts so far. Just a few pointers.
If possible leave a little white space somewhere on the business card incase someone wants to write on it. I write on business cards all the time.
I do prefer the dark background/light symbol. Also please try to incorporate the designed website address.
Thanks for your efforts so far and keep them coming!
Hi,
Please can you also provide samples of letterheaded paper and compliment slips as I would like the same theme carried through.
Thanks and keep up the good work!
Can you also try the dark background with the lighter symbol for the front of the business card.

```html
<!DOCTYPE html>
<html lang="en">
<head>
<meta charset="utf-8">
<title>Coldbrook IT — Stationery Set</title>
<link rel="stylesheet" href="https://fonts.googleapis.com/css2?family=Open+Sans:wght@400;600;700&display=swap">
<style>
  :root {
    --stage: #5b5c5e;
    --brand-blue: #1ba8e0;
    --paper: #ffffff;
    --ink: #2f3a44;
    --muted: #8a9299;
    --table-grey: #cfd1d3;
    --window-grey: #c9cacb;
    --hub-dark: #2a2b2d;
    --watermark: #ececee;
  }
  * { box-sizing: border-box; margin: 0; padding: 0; }
  html, body { width: 1200px; height: 605px; overflow: hidden; }
  body {
    position: relative;
    background: var(--stage);
    font-family: "Open Sans", Arial, sans-serif;
    color: var(--ink);
  }
  .item { position: absolute; background: var(--paper); overflow: hidden; }

  .brand { display: flex; flex-direction: column; align-items: center; font-weight: 700; color: var(--brand-blue); line-height: 1; }
  .brand .brand-mark { width: 10px; height: 10px; background: currentColor; margin-bottom: 3px; }
  .brand .brand-name { font-size: 8px; letter-spacing: 0.3px; white-space: nowrap; }
  .brand.on-blue { color: var(--paper); }

  /* Business card front */
  .card-front { left: 29px; top: 34px; width: 235px; height: 127px; background: var(--brand-blue); }
  .card-front svg { position: absolute; inset: 0; }
  .card-front .holder-name { position: absolute; left: 78px; top: 30px; color: var(--paper); font-weight: 700; font-size: 11px; letter-spacing: 0.5px; white-space: nowrap; }
  .card-front .holder-role { position: absolute; left: 106px; top: 46px; color: #d9f1fb; font-size: 5.5px; white-space: nowrap; }

  /* Business card back */
  .card-back { left: 29px; top: 175px; width: 235px; height: 132px; }
  .card-back .band { position: absolute; left: 0; right: 0; top: 65px; height: 38px; background: var(--brand-blue); }
  .card-back .brand { position: absolute; left: 6px; top: 58px; background: var(--paper); padding: 5px 4px; }
  .card-back .contact { position: absolute; left: 150px; top: 70px; color: var(--paper); font-size: 5px; line-height: 7.5px; white-space: nowrap; }

  /* Envelope */
  .envelope { left: 29px; top: 324px; width: 331px; height: 221px; }
  .envelope svg.flap { position: absolute; left: 0; top: 0; }
  .envelope .brand { position: absolute; left: 155px; top: 16px; transform: translateX(-50%); }
  .envelope .address-window { position: absolute; left: 12px; top: 103px; width: 170px; height: 50px; background: var(--window-grey); border-radius: 7px; }
  .footer-line { position: absolute; font-size: 4.5px; color: var(--muted); white-space: nowrap; }
  .envelope .footer-line { left: 14px; bottom: 10px; }

  /* Letterhead & invoice */
  .sheet { top: 29px; height: 559px; }
  .letterhead { left: 372px; width: 372px; }
  .invoice { left: 773px; width: 396px; }
  .sheet .rule-left { position: absolute; left: 12px; top: 12px; bottom: 20px; width: 1.5px; background: var(--brand-blue); }
  .sheet .rule-top { position: absolute; left: 12px; right: 8px; top: 38px; height: 1px; background: var(--brand-blue); }
  .sheet .rule-bottom { position: absolute; left: 12px; right: 8px; bottom: 30px; height: 1px; background: var(--brand-blue); }
  .sheet .brand { position: absolute; left: 30px; top: 10px; }
  .sheet .footer-line { left: 40px; bottom: 18px; }
  .watermark { position: absolute; font-weight: 700; color: var(--watermark); font-size: 36px; white-space: nowrap; }
  .letterhead .watermark { left: 70px; top: 236px; }
  .invoice .watermark { left: 95px; top: 236px; }

  .invoice-title { position: absolute; left: 254px; top: 56px; font-size: 8px; font-weight: 700; }
  .invoice-date { position: absolute; left: 254px; top: 68px; font-size: 7px; }
  .bill-to { position: absolute; left: 24px; top: 88px; font-size: 9px; font-weight: 700; }
  .invoice-table { position: absolute; left: 24px; top: 115px; width: 356px; height: 233px; }
  .invoice-table .head { position: absolute; left: 0; right: 0; top: 0; height: 17px; background: var(--table-grey); font-size: 7px; font-weight: 600; }
  .invoice-table .head span { position: absolute; top: 4px; }
  .invoice-table .divider { position: absolute; left: 242px; top: 17px; bottom: 17px; width: 1px; background: var(--table-grey); }
  .invoice-table .total { position: absolute; left: 0; right: 0; bottom: 0; height: 17px; background: var(--table-grey); font-size: 7px; font-weight: 600; }
  .invoice-table .total span { position: absolute; left: 248px; top: 4px; }

  /* Disc */
  .disc { position: absolute; left: 559px; top: 175px; }
</style>
</head>
<body>

  <section class="item card-front" aria-label="Business card front">
    <svg width="235" height="127" viewBox="0 0 235 127" aria-hidden="true">
      <polygon points="62,127 235,58 235,76 98,127" fill="#ffffff" opacity="0.9"/>
      <polygon points="98,127 235,76 235,83 116,127" fill="#ffffff" opacity="0.5"/>
    </svg>
    <div class="holder-name">DECLAN MORAN</div>
    <div class="holder-role">IT Consultant</div>
  </section>

  <section class="item card-back" aria-label="Business card back">
    <div class="band"></div>
    <div class="brand"><span class="brand-mark"></span><span class="brand-name">Coldbrook IT</span></div>
    <div class="contact">
      Tel 028 7135 0194<br>
      info@coldbrookit.co.uk<br>
      www.coldbrookit.co.uk<br>
      12 Mill Road, Derry
    </div>
  </section>

  <section class="item envelope" aria-label="Envelope">
    <svg class="flap" width="331" height="50" viewBox="0 0 331 50" aria-hidden="true">
      <path d="M0 0 H331 V18 L180 48 Q165 51 150 48 L0 18 Z" fill="var(--brand-blue)"/>
    </svg>
    <div class="brand on-blue"><span class="brand-mark"></span><span class="brand-name">Coldbrook IT</span></div>
    <div class="address-window"></div>
    <div class="footer-line">www.coldbrookit.co.uk &nbsp;|&nbsp; info@coldbrookit.co.uk &nbsp;|&nbsp; Tel 028 7135 0194</div>
  </section>

  <section class="item sheet letterhead" aria-label="Letterhead">
    <div class="rule-left"></div>
    <div class="rule-top"></div>
    <div class="brand"><span class="brand-mark"></span><span class="brand-name">Coldbrook IT</span></div>
    <div class="watermark">Coldbrook IT</div>
    <div class="rule-bottom"></div>
    <div class="footer-line">www.coldbrookit.co.uk &nbsp;|&nbsp; info@coldbrookit.co.uk &nbsp;|&nbsp; Tel 028 7135 0194</div>
  </section>

  <section class="item sheet invoice" aria-label="Invoice">
    <div class="rule-left"></div>
    <div class="brand"><span class="brand-mark"></span><span class="brand-name">Coldbrook IT</span></div>
    <div class="watermark">Coldbrook IT</div>
    <div class="invoice-title">INVOICE</div>
    <div class="invoice-date">Date :-</div>
    <div class="bill-to">BILL TO:</div>
    <div class="invoice-table">
      <div class="head"><span style="left:6px">DESCRIPTION</span><span style="left:248px">AMOUNT</span></div>
      <div class="divider"></div>
      <div class="total"><span>TOTAL</span></div>
    </div>
    <div class="rule-bottom"></div>
    <div class="footer-line">www.coldbrookit.co.uk &nbsp;|&nbsp; info@coldbrookit.co.uk &nbsp;|&nbsp; Tel 028 7135 0194</div>
  </section>

  <svg class="disc" width="298" height="298" viewBox="0 0 298 298" aria-label="CD disc">
    <circle cx="149" cy="149" r="149" fill="var(--brand-blue)"/>
    <circle cx="149" cy="149" r="148" fill="none" stroke="#ffffff" stroke-opacity="0.4"/>
    <g stroke="#ffffff" stroke-width="1.2">
      <line x1="53" y1="168" x2="137" y2="168"/>
      <line x1="53" y1="185" x2="137" y2="185"/>
      <line x1="53" y1="202" x2="137" y2="202"/>
    </g>
    <circle cx="149" cy="149" r="43" fill="var(--hub-dark)"/>
    <circle cx="149" cy="149" r="28" fill="#444547"/>
    <circle cx="149" cy="149" r="14" fill="var(--stage)"/>
  </svg>

</body>
</html>
```